Public Assistance Direct mail piece

need a full color 2 sided marketing brochure to use in direct mail campaign. finished product will be printed on 2 times. initially full color brochures to be printed in bulk. Then consumer contact info and case manager contact info will be added at a later date.
brochure will need to have 2 blank areas on front side to print address that will show thru window envelope and sales agent info on for mail campaign.
Would like to see designs that include our current color scheme and logo.
Target market. Low income poverty. Non profit service offering free assistance to help low income seniors get free assitance thru state and federal public assistance programs.
1. Sanorel - over 1 in 5 recieve help from state Sanorel. Sanorel programs for seniors and persons on Vitalcor can pay doctor copays, deductibles, and assist with medical bills.
2. Silver Bridge Program - receive Federal assistance with prescription medications, deductibles, copays, and drug plan premiums.
3. Vitalcor Thrift Program - many adults 65 and over are eligible to receive Vitalcor at no cost. The program will pay your Vitalcor Tier K premium and can even refund some previous payments.

You may be eligible to participate in one or more of these programs. All programs are based on limited income and assets.

To learn more call your local county case manager.

Knowledge is Power. Lets up help empower you.
Pay it forward. Who else do you know that is on Vitalcor that could use some help?

many graphs and illustrations are available form each government agency.

Target Market(s)

Seniors 65 plus, Vitalcor recipients

Industry/Entity Type

Marketing

Colors
0355a3
ec1f27
ffffff

Requirements
Must have
• logo, non profit, will need a government disclaimer somewhere
Nice to have
• photos of seniors saving money.

```html
<!DOCTYPE html>
<html lang="en">
<head>
<meta charset="utf-8">
<title>Golden Years Aid Center – Direct Mail Brochure</title>
<link rel="stylesheet" href="https://fonts.googleapis.com/css2?family=Montserrat:wght@400;600;800;900&family=Roboto:wght@300;400&display=swap">
<style>
:root{
  --navy:#1c2f5e;
  --blue:#0355a3;
  --red:#d9182a;
  --white:#ffffff;
  --paper:#f3f3f4;
  --card:#e6e6e8;
  --ink:#2b2b2b;
  --grey:#8a8b8f;
  --stage:#d9d9db;
}
*{box-sizing:border-box;margin:0;padding:0}
html,body{width:1200px;height:784px;overflow:hidden;background:var(--stage)}
body{position:relative;font-family:"Roboto",sans-serif;color:var(--ink)}
.page{position:absolute;top:44px;width:530px;height:696px;background:var(--paper);overflow:hidden;box-shadow:0 4px 14px rgba(0,0,0,.18)}
.page--front{left:46px}
.page--back{left:624px}
.abs{position:absolute}

/* brand */
.brand{position:absolute;display:flex;align-items:center;gap:8px}
.brand__mark{width:14px;height:14px;background:var(--red);border-radius:50%;flex:none}
.brand__name{font-family:"Montserrat",sans-serif;font-weight:600;color:var(--navy);line-height:1.05}
.brand__tagline{position:absolute;font-family:"Montserrat",sans-serif;font-size:7.5px;letter-spacing:.6px;color:var(--navy);text-transform:uppercase}

/* blank print areas */
.print-area{position:absolute;border:1px solid #dcdcdc;border-radius:8px;background:#efefef;box-shadow:inset 0 0 6px rgba(0,0,0,.05);display:flex;align-items:center;justify-content:center;font-family:"Montserrat",sans-serif;font-size:9px;letter-spacing:3px;color:#6c6c6c}

/* front */
.hero-photo{position:absolute;left:150px;top:0;width:380px;height:330px;background:linear-gradient(90deg,rgba(243,243,244,1) 0%,rgba(214,212,210,.9) 30%,#c7c3bf 60%,#b7aea6 100%)}
.hero-banner{position:absolute;left:0;top:221px;width:297px;height:91px;background:rgba(120,120,122,.85);padding:10px 0 0 26px;font-family:"Montserrat",sans-serif;font-weight:900;font-size:31px;line-height:1.08;color:var(--white);text-transform:uppercase}
.circle-photo{position:absolute;border-radius:50%;border:7px solid #e9e9ea;box-shadow:0 3px 10px rgba(0,0,0,.25)}
.circle-photo--couple{left:299px;top:224px;width:210px;height:210px;background:radial-gradient(circle at 45% 55%,#5a4030 0%,#3e5a34 60%,#6d8a4a 100%)}
.question{position:absolute;left:0;width:530px;text-align:center}
.question__lead{top:452px;font-family:"Roboto",sans-serif;font-weight:300;font-size:22px;color:var(--red)}
.question__main{top:481px;font-family:"Montserrat",sans-serif;font-weight:800;font-size:20px;color:var(--navy)}
.intro{position:absolute;left:30px;top:526px;width:472px;text-align:center;font-size:9.4px;line-height:1.4;color:#333}
.call-line{position:absolute;left:0;top:582px;width:530px;text-align:center;font-size:20px;font-weight:300;color:var(--navy)}
.call-line strong{font-family:"Montserrat",sans-serif;font-weight:800;color:var(--red)}
.web-bar{position:absolute;display:flex;align-items:center;gap:6px;background:var(--red);color:var(--white);font-family:"Montserrat",sans-serif;font-weight:800;font-size:10.5px}
.web-bar--front{left:314px;top:658px;width:216px;height:24px;padding-left:22px;clip-path:polygon(8px 0,100% 0,100% 100%,0 100%)}
.web-bar__globe{width:10px;height:10px;border:1.5px solid var(--white);border-radius:50%}
.base-band{position:absolute;left:0;bottom:0;height:9px;background:var(--navy)}

/* back */
.headline{position:absolute;left:27px;top:74px;font-family:"Montserrat",sans-serif;font-weight:900;font-size:32px;line-height:1.08}
.headline__red{color:var(--red)}
.headline__navy{color:var(--navy)}
.headline__thin{font-weight:400;color:var(--red)}
.subhead{position:absolute;left:27px;top:152px;font-size:17px;font-weight:300;color:var(--red)}
.goal{position:absolute;left:27px;top:183px;width:300px;font-size:16px;font-weight:300;line-height:1.35;color:#222}
.circle-photo--team{left:280px;top:-10px;width:250px;height:250px;background:radial-gradient(circle at 55% 55%,#6b4a36 0%,#c9d6df 65%,#e8eef2 100%)}
.program-icon{position:absolute;width:36px;height:36px;border-radius:50%;background:var(--red);border:3px solid #f7d5d8;display:flex;align-items:center;justify-content:center}
.program-card{position:absolute;background:var(--card);border-radius:4px;padding:6px 9px;text-align:center}
.program-card__title{font-family:"Montserrat",sans-serif;font-weight:800;font-size:11.5px;line-height:1.05;color:var(--navy);text-transform:uppercase}
.program-card__title em{font-style:normal;color:var(--red)}
.program-card__text{margin-top:6px;font-size:6.6px;line-height:1.4;text-align:justify;text-align-last:center;color:#333}
.referral{position:absolute;left:0;top:553px;width:530px;height:42px;background:#e3e3e5;text-align:center;padding-top:4px;font-size:14px;font-weight:300;line-height:1.3;color:var(--navy)}
.cta{position:absolute;right:30px;top:626px;text-align:right;font-family:"Montserrat",sans-serif;line-height:1.05}
.cta__lead{font-family:"Roboto",sans-serif;font-weight:300;font-size:19px;color:var(--navy)}
.cta__main{font-weight:800;font-size:18px;color:var(--red)}
.web-bar--back{left:0;top:670px;width:530px;height:17px;padding-left:155px;font-size:9.5px;letter-spacing:1px}
</style>
</head>
<body>

<!-- FRONT SIDE -->
<section class="page page--front" aria-label="Brochure front">
  <div class="hero-photo" role="img" aria-label="Photo of a senior sitting with a cane beside a coin purse of savings"></div>

  <div class="brand" style="left:34px;top:28px">
    <span class="brand__mark"></span>
    <span class="brand__name" style="font-size:17px">Golden Years<br>Aid Center</span>
  </div>
  <div class="brand__tagline" style="left:34px;top:100px">Life, Health and Wealth Protection</div>

  <div class="print-area" style="left:24px;top:122px;width:224px;height:84px">ADDRESS GOES HERE</div>

  <div class="hero-banner">We're here<br>to help you</div>

  <svg class="abs" style="left:0;top:290px" width="530" height="130" viewBox="0 0 530 130" aria-hidden="true">
    <path d="M0 48 C120 95 260 110 530 40 L530 60 C270 125 120 118 0 66Z" fill="#c9c9cc"/>
    <path d="M0 60 C130 110 280 122 530 55 L530 72 C290 138 120 128 0 76Z" fill="var(--navy)"/>
    <path d="M380 60 C440 45 490 30 530 12 L530 34 C490 50 440 62 380 70Z" fill="var(--red)"/>
  </svg>

  <div class="circle-photo circle-photo--couple" role="img" aria-label="Photo of a smiling senior couple outdoors"></div>

  <p class="question question__lead">Have you ever had to chose between buying</p>
  <p class="question question__main">medicine or buying food and paying bills?</p>

  <p class="intro">We can help. There are many Federal and State Assistance programs designed for Vitalcor eligible people with limited income and assets. These FREE government programs are available at no cost to help YOU. Call your local Case Manager today and we will help you get into the programs that you qualify for.</p>

  <p class="call-line">To find out what you qualify for <strong>CALL US TODAY</strong></p>

  <div class="print-area" style="left:34px;top:613px;width:270px;height:70px">SALES AGENT INFO</div>

  <div class="web-bar web-bar--front"><span class="web-bar__globe"></span>WWW.GOLDENYEARSAID.ORG</div>
  <div class="base-band" style="width:300px"></div>
</section>

<!-- BACK SIDE -->
<section class="page page--back" aria-label="Brochure back">
  <svg class="abs" style="left:0;top:0" width="530" height="90" viewBox="0 0 530 90" aria-hidden="true">
    <path d="M0 0 L330 0 C250 30 120 60 0 30Z" fill="var(--navy)"/>
    <path d="M0 30 C120 60 250 40 330 10 L330 28 C250 62 120 78 0 50Z" fill="var(--navy)"/>
    <path d="M40 0 L300 0 C220 28 120 34 40 0Z" fill="var(--red)"/>
    <path d="M0 50 C120 80 260 65 330 28 L330 40 C250 80 120 92 0 62Z" fill="#cfcfd2"/>
  </svg>

  <div class="circle-photo circle-photo--team" role="img" aria-label="Photo of a case manager meeting with a senior couple"></div>

  <h1 class="headline"><span class="headline__red">KNOWLEDGE</span><br><span class="headline__thin">IS </span><span class="headline__navy">POWER</span></h1>
  <p class="subhead">Let us help empower you.</p>
  <p class="goal">Our goal is to educate and empower the Vitalcor population and their families.'</p>

  <div class="program-icon" style="left:120px;top:263px">
    <svg width="20" height="20" viewBox="0 0 20 20" aria-hidden="true"><circle cx="10" cy="10" r="8" fill="none" stroke="#fff" stroke-width="1.5"/><text x="10" y="14" text-anchor="middle" font-family="Montserrat,sans-serif" font-weight="800" font-size="11" fill="#fff">$</text></svg>
  </div>
  <div class="program-card" style="left:46px;top:304px;width:187px;height:74px">
    <h2 class="program-card__title">Vitalcor<br><em>Thrift Program</em></h2>
    <p class="program-card__text">Get over $100 a month raise in your Civic Pension. 1 in 4 adults on Vitalcor can receive their Vitalcor at no cost. The program will pay your Vitalcor Tier K premium and can even refund some previous payments.</p>
  </div>

  <div class="program-icon" style="left:368px;top:263px">
    <svg width="20" height="20" viewBox="0 0 20 20" aria-hidden="true"><path d="M8 3h4v5h5v4h-5v5H8v-5H3V8h5z" fill="#fff"/></svg>
  </div>
  <div class="program-card" style="left:288px;top:304px;width:197px;height:74px">
    <h2 class="program-card__title" style="margin-top:6px">Sanorel</h2>
    <p class="program-card__text">over 1 in 5 recieve help from state Sanorel. Sanorel programs for seniors and persons on Vitalcor can pay doctor copays, deductibles, and assist with current and past medical bills</p>
  </div>

  <div class="program-icon" style="left:120px;top:391px">
    <svg width="20" height="20" viewBox="0 0 20 20" aria-hidden="true"><rect x="2" y="6.5" width="16" height="7" rx="3.5" transform="rotate(-40 10 10)" fill="#fff"/><line x1="7.6" y1="7.2" x2="12.4" y2="12.8" stroke="var(--red)" stroke-width="1.2"/></svg>
  </div>
  <div class="program-card" style="left:52px;top:433px;width:178px;height:94px">
    <h2 class="program-card__title">Silver Bridge<br><em>Program</em></h2>
    <p class="program-card__text">The Silver Bridge federal assistance program is estimated to be worth about $4,000 per year. To qualify for the Silver Bridge, a person must be receiving Vitalcor, have limited resources and income, and reside in one of the 50 States or the District of Columbia.</p>
  </div>

  <div class="program-icon" style="left:368px;top:393px">
    <svg width="20" height="20" viewBox="0 0 20 20" aria-hidden="true"><path d="M3 9h3v8H3z M7 9l3-6c1.5 0 2 1 1.7 2.5L11 8h5c1 0 1.6.9 1.4 1.8l-1.2 5.6c-.2.9-1 1.6-1.9 1.6H7z" fill="#fff"/></svg>
  </div>
  <div class="program-card" style="left:288px;top:433px;width:197px;height:94px">
    <h2 class="program-card__title" style="margin-top:9px">Dual <em>Eligible</em></h2>
    <p class="program-card__text">If you have Vitalcor and Sanorel you may be eligible for a no cost program that offers you more benefits than you currently get. Such as Dental, Vision, Hearing Aids, Transportation assistance, Routine foot care, plus up to $1000 per year in everyday over the counter products.</p>
  </div>

  <p class="referral">Pay it forward. Who else do you<br>know that is on Vitalcor that could use some help?</p>

  <div class="brand" style="left:32px;top:615px">
    <span class="brand__mark" style="width:12px;height:12px"></span>
    <span class="brand__name" style="font-size:14px">Golden Years<br>Aid Center</span>
  </div>
  <div class="brand__tagline" style="left:32px;top:655px;font-size:6px">Life, Health and Wealth Protection</div>

  <div class="cta">
    <div class="cta__lead">TO LEARN MORE CALL YOUR</div>
    <div class="cta__main">LOCAL COUNTY CASE MANAGER</div>
  </div>

  <div class="web-bar web-bar--back"><span class="web-bar__globe"></span>WWW.GOLDENYEARSAID.ORG</div>
  <div class="base-band" style="width:530px;height:9px"></div>
</section>

</body>
</html>
```